Business Card Design Project

I need a business card with the logo i have selected with a heading of
Repairs
Restretching
Cleaning
Supply and lay all in that order
call 0438271946
www.rugmendhouse.example

colours used should be bold and clear and match the logo, thinking white background with black writing
a mixture of fonts is okay but Repairs, Cleaning, Supply and Lay should all be the same as they are the main points...
kind regards lorn
update to all designers i would like my name on the business card Lorn Tabbet i think it would look good above the phone number
Updates

can you please add my name on the business card

Lorn Tabbet

i think it would look best above the phone numberĀ 

Industry/Entity Type

Business

```html
<!DOCTYPE html>
<html lang="en">
<head>
<meta charset="utf-8">
<title>Rug Mend House – Business Card</title>
<link href="https://fonts.googleapis.com/css2?family=Righteous&family=Dancing+Script:wght@600&family=Roboto:wght@400;700&display=swap" rel="stylesheet">
<style>
  :root {
    --navy: #173a5e;
    --ink: #1f1a17;
    --red: #e0262b;
    --white: #ffffff;
    --tan: #d8b47e;
    --hair: #f3a238;
  }
  * { margin: 0; padding: 0; box-sizing: border-box; }
  html, body { width: 1200px; height: 693px; overflow: hidden; background: var(--white); }
  .card { position: relative; width: 1200px; height: 693px; background: var(--white); overflow: hidden; }

  .band { position: absolute; left: 0; width: 100%; height: 16px; background: var(--navy); }
  .band--top { top: 0; }
  .band--bottom { bottom: 0; }

  .backdrop-figure {
    position: absolute; left: 640px; top: 20px; width: 560px; height: 657px;
    background: radial-gradient(ellipse at 50% 45%, rgba(243,162,56,0.07), rgba(216,180,126,0.04) 55%, rgba(255,255,255,0) 75%);
  }

  .mascot {
    position: absolute; left: 100px; top: 66px; width: 430px; height: 370px;
    border-radius: 24px;
    background: linear-gradient(180deg, rgba(243,162,56,0.5) 0%, rgba(216,180,126,0.55) 50%, rgba(232,232,232,0.7) 100%);
  }

  .brand-name {
    position: absolute; left: 60px; top: 488px; width: 510px;
    text-align: center; white-space: nowrap; color: var(--navy);
    font-family: "Righteous", sans-serif; font-weight: 400;
    font-size: 50px; line-height: 60px; letter-spacing: 1px;
  }

  .details { position: absolute; left: 540px; top: 0; width: 620px; height: 100%; text-align: center; }
  .details__title {
    position: absolute; top: 88px; width: 100%; white-space: nowrap;
    font-family: "Righteous", sans-serif; font-weight: 400; font-size: 60px; line-height: 64px;
    color: var(--ink); letter-spacing: 1px;
  }
  .services { list-style: none; position: absolute; top: 156px; width: 100%; }
  .services li {
    font-family: "Dancing Script", cursive; font-weight: 600;
    font-size: 62px; line-height: 62px; color: var(--ink);
  }
  .owner {
    position: absolute; top: 408px; width: 100%;
    font-family: "Roboto", sans-serif; font-weight: 400; font-size: 30px; line-height: 36px;
    color: var(--ink); letter-spacing: 1px;
  }
  .phone {
    position: absolute; top: 448px; width: 100%; height: 84px;
    display: flex; justify-content: center; align-items: center; gap: 18px;
    font-family: "Roboto", sans-serif; font-weight: 700; font-size: 72px; line-height: 84px; color: var(--ink);
  }
  .phone__icon { width: 50px; height: 50px; flex: none; }
  .web {
    position: absolute; top: 545px; width: 100%; white-space: nowrap;
    font-family: "Roboto", sans-serif; font-weight: 400; font-size: 42px; line-height: 50px; color: var(--ink);
  }
</style>
</head>
<body>
<main class="card">
  <div class="band band--top"></div>

  <div class="backdrop-figure" role="img" aria-label="Faint enlarged mascot illustration in the background"></div>

  <div class="mascot" role="img" aria-label="Cartoon carpet repairer mascot carrying a rolled carpet and a first-aid case"></div>

  <p class="brand-name">RUG MEND HOUSE</p>

  <section class="details">
    <h1 class="details__title">RUG MEND HOUSE</h1>
    <ul class="services">
      <li>Repairs</li>
      <li>Restretching</li>
      <li>Cleaning</li>
      <li>Supply &amp; Lay</li>
    </ul>
    <p class="owner">Lorn Tabbet</p>
    <p class="phone">
      <svg class="phone__icon" viewBox="0 0 46 46" aria-hidden="true">
        <circle cx="23" cy="23" r="20.5" fill="none" stroke="#e0262b" stroke-width="3"/>
        <path d="M17 12c-2 1-4 3-4 6 0 7 8 16 15 16 3 0 5-2 6-4l-4-4c-1 1-2 2-3 2-3-1-7-5-8-8 0-1 1-2 2-3z" fill="#e0262b"/>
      </svg>
      <span>0438271946</span>
    </p>
    <p class="web">www.rugmendhouse.example</p>
  </section>

  <div class="band band--bottom"></div>
</main>
</body>
</html>
```